TREMLUX electrical and air conditioning

the van(KMR vantrek 5 LWB in Australia) wrap design features a dynamic and eye-catching layout that enhances brand visibility while reflecting our core values and mission.
A vibrant color scheme, captures attention and evokes emotions associated with our brand. The colors are strategically placed to create a sense of movement and energy.Graphics: Bold, high-resolution graphics highlight our key services, which are refrigeration and electrical.

Target Market(s)

Locals

Requirements
Must have
• services including : Electrical/air conditioning / refrigeration / data

```html
<!DOCTYPE html>
<html lang="en">
<head>
<meta charset="utf-8">
<title>TREMLUX van wrap</title>
<link rel="stylesheet" href="https://fonts.googleapis.com/css2?family=Russo+One&family=Saira+Semi+Condensed:wght@600;700&family=Montserrat:wght@700;800&display=swap">
<style>
:root{
  --bg:#e9ebee;
  --ink:#0b0a0c;
  --blue:#1a7fd0;
  --blue-deep:#0f5fae;
  --sky:#3aa6f0;
  --yellow:#e6b100;
  --orange:#f08a10;
  --orange-deep:#e9581a;
  --white:#ffffff;
  --grey:#d7d7d7;
}
*{margin:0;padding:0;box-sizing:border-box}
html,body{width:1200px;height:1046px;overflow:hidden;background:var(--bg)}
.canvas{position:relative;width:1200px;height:1046px}
.side-panel{position:absolute;left:20px;top:30px;width:1160px;height:480px;border-radius:60px 40px 28px 70px;overflow:hidden}
.rear-panel{position:absolute;left:310px;top:545px;width:580px;height:480px;border-radius:40px 40px 26px 26px;overflow:hidden}
.panel-art{position:absolute;inset:0;width:100%;height:100%}

.wordmark{position:absolute;font-family:"Russo One",sans-serif;font-weight:400;color:var(--orange);letter-spacing:2px;line-height:1;text-align:center;white-space:nowrap}
.side-panel .wordmark{left:490px;top:150px;width:420px;font-size:70px}
.rear-panel .wordmark{left:90px;top:192px;width:400px;font-size:56px}

.mark-dot{position:absolute;border-radius:50%;background:var(--sky)}
.side-panel .mark-dot{left:680px;top:82px;width:40px;height:40px}
.rear-panel .mark-dot{left:273px;top:138px;width:34px;height:34px}

.estd{position:absolute;font-family:"Montserrat",sans-serif;font-weight:700;color:var(--grey);letter-spacing:1px;line-height:1}
.side-panel .estd{top:114px;font-size:12px}
.rear-panel .estd{top:162px;font-size:10px}

.tagline{position:absolute;font-family:"Saira Semi Condensed",sans-serif;font-weight:700;color:var(--white);letter-spacing:2px;text-align:center;line-height:1;white-space:nowrap}
.side-panel .tagline{left:550px;top:234px;width:300px;font-size:14px}
.rear-panel .tagline{left:130px;top:260px;width:320px;font-size:11px}

.contact{position:absolute;left:470px;top:368px;font-family:"Saira Semi Condensed",sans-serif;font-weight:700;color:var(--white);font-size:34px;line-height:1;letter-spacing:0.5px}
.contact span{display:block;margin-bottom:4px}

.service-list{position:absolute;left:960px;top:120px;list-style:none}
.service-list li{width:150px;height:24px;margin-bottom:11px;border:2px solid var(--sky);border-radius:5px;background:linear-gradient(var(--blue),var(--blue-deep));font-family:"Russo One",sans-serif;color:var(--ink);font-size:12px;text-align:center;line-height:20px;letter-spacing:0.5px;white-space:nowrap}
.service-list li.wide{font-size:10.5px}

.badge{position:absolute;border-radius:50%;border:3px solid var(--white);color:var(--white);text-align:center;font-family:"Montserrat",sans-serif;font-weight:800;font-style:italic;display:flex;flex-direction:column;justify-content:center;align-items:center;line-height:1}
.side-panel .badge{left:250px;top:258px;width:116px;height:116px;gap:2px}
.side-panel .badge .num{font-size:34px}
.side-panel .badge .small{font-size:8px;letter-spacing:0.5px}
.side-panel .badge .mid{font-size:13px}
.rear-panel .badge{left:474px;top:294px;width:56px;height:56px;border-width:2px;gap:1px}
.rear-panel .badge .num{font-size:15px}
.rear-panel .badge .small{font-size:4px}
.rear-panel .badge .mid{font-size:6px}

.strap{position:absolute;left:0;top:30px;width:100%;text-align:center;font-family:"Montserrat",sans-serif;font-weight:700;color:var(--white);font-size:15px;letter-spacing:0.5px}
.contact-band{position:absolute;left:22px;top:368px;width:536px;height:30px;background:var(--sky);display:flex;font-family:"Saira Semi Condensed",sans-serif;font-weight:700;color:var(--white);font-size:20px;line-height:30px}
.contact-band span{flex:1;text-align:center}
.rear-services{position:absolute;left:40px;top:412px;width:500px;display:grid;grid-template-columns:1fr 1fr;row-gap:6px;font-family:"Russo One",sans-serif;color:var(--ink);font-size:15px;letter-spacing:0.5px;white-space:nowrap}
.rear-services span::before{content:"";display:inline-block;width:9px;height:9px;border-radius:50%;background:var(--sky);margin-right:6px;vertical-align:1px}
</style>
</head>
<body>
<main class="canvas">
  <section class="side-panel" aria-label="Van side wrap">
    <svg class="panel-art" viewBox="0 0 1160 480" preserveAspectRatio="none" aria-hidden="true">
      <defs>
        <linearGradient id="sweep" x1="0" y1="0" x2="1" y2="0">
          <stop offset="0" stop-color="#e6b100"/><stop offset="1" stop-color="#f08a10"/>
        </linearGradient>
      </defs>
      <rect width="1160" height="480" fill="#0b0a0c"/>
      <path d="M0 0 H600 C520 180 420 330 290 480 H0 Z" fill="url(#sweep)"/>
      <path d="M0 0 H535 C470 170 370 320 250 440 L230 480 H0 Z" fill="#1a7fd0"/>
      <path d="M520 0 H535 C470 170 370 320 250 440 L240 450 C360 320 460 170 520 0 Z" fill="#0b0a0c"/>
      <path d="M700 480 C820 360 960 300 1160 290 V480 Z" fill="url(#sweep)"/>
      <path d="M690 480 C800 340 950 270 1160 250 V285 C950 300 820 360 715 480 Z" fill="#1a7fd0"/>
    </svg>
    <div class="mark-dot" aria-hidden="true"></div>
    <span class="estd" style="left:600px">ESTD.</span>
    <span class="estd" style="left:766px">2020</span>
    <div class="wordmark">TREMLUX</div>
    <div class="tagline">ELECTRICAL &amp; AIR CONDITIONING</div>
    <div class="badge"><span class="small">EMERGENCY</span><span class="num">24</span><span class="mid">HOUR</span><span class="small">SERVICE</span></div>
    <div class="contact"><span>(555) 014-2870</span><span>tremluxco.com</span></div>
    <ul class="service-list">
      <li>ELECTRICAL</li>
      <li class="wide">AIR CONDITIONING</li>
      <li class="wide">REFRIGERATION</li>
      <li>&amp; DATA</li>
    </ul>
  </section>

  <section class="rear-panel" aria-label="Van rear wrap">
    <svg class="panel-art" viewBox="0 0 580 480" preserveAspectRatio="none" aria-hidden="true">
      <defs>
        <linearGradient id="rearSweep" x1="0" y1="0" x2="1" y2="0">
          <stop offset="0" stop-color="#e9581a"/><stop offset="0.5" stop-color="#e6b100"/><stop offset="1" stop-color="#e9581a"/>
        </linearGradient>
      </defs>
      <rect width="580" height="480" fill="#0b0a0c"/>
      <rect y="398" width="580" height="82" fill="url(#rearSweep)"/>
      <line x1="290" y1="0" x2="290" y2="480" stroke="#2a2a2a" stroke-width="1.5"/>
    </svg>
    <div class="strap">Proudly Serving Your community!</div>
    <div class="mark-dot" aria-hidden="true"></div>
    <span class="estd" style="left:180px">ESTD.</span>
    <span class="estd" style="left:360px">2020</span>
    <div class="wordmark">TREMLUX</div>
    <div class="tagline">ELECTRICAL &amp; AIR CONDITIONING</div>
    <div class="badge"><span class="small">EMERGENCY</span><span class="num">24</span><span class="mid">HOUR</span><span class="small">SERVICE</span></div>
    <div class="contact-band"><span>(555) 014-2870</span><span>tremluxco.com</span></div>
    <div class="rear-services">
      <span>ELECTRICAL</span><span>AIR CONDITIONING</span>
      <span>REFRIGERATION</span><span>&amp; DATA</span>
    </div>
  </section>
</main>
</body>
</html>
```